Pim Tavel Brochure Design

We are a Marketing company offering different services. Services must be outlined on design we will provive text for the services once project is accepted.

Service Titles to include in design

Corporate Branding
Marketing
Web Design 
Business Consultation
Printing
Mailing
Automation
Pim Tavel Choice

Please post designs, we have n

Target Market(s)

18+ Years Old

Must have
• Web 2.0 Graphics
• Eye catching design
Nice to have
• Rich Graphics
• Creativity
Should not have
• Standard Templates
• Only bullets

```html
<!DOCTYPE html>
<html lang="en">
<head>
<meta charset="utf-8">
<title>Pim Tavel Marketing – Services Brochure</title>
<link href="https://fonts.googleapis.com/css2?family=Exo+2:wght@600&family=Arimo:wght@400&display=swap" rel="stylesheet">
<style>
  :root {
    --ink: #040606;
    --panel-dark: #1f2326;
    --accent: #fbaa2f;
    --text: #ffffff;
    --grey-top: #858080;
    --grey-mid: #bdbbbb;
    --paper: #ffffff;
    --name-grey: #4a4a4a;
  }
  * { margin: 0; padding: 0; box-sizing: border-box; }
  html, body { width: 1200px; height: 848px; overflow: hidden; background: var(--ink); }
  .brochure { position: relative; width: 1200px; height: 848px; background: var(--ink); }

  .cover {
    position: absolute; left: 0; top: 0; width: 400px; height: 848px;
    background: linear-gradient(to bottom, var(--grey-top) 0%, var(--grey-mid) 45%, #f4f4f4 80%, var(--paper) 100%);
  }
  .cover svg, .fold svg { position: absolute; left: 0; top: 0; }

  .company-name {
    position: absolute; right: 24px; top: 784px;
    font-family: "Exo 2", sans-serif; font-weight: 600; font-size: 26px;
    line-height: 1; color: var(--name-grey);
  }

  .fold { position: absolute; top: 0; height: 848px; background: var(--ink); }
  .fold-middle { left: 408px; width: 384px; }
  .fold-right { left: 800px; width: 400px; }

  .service { position: absolute; left: 17px; width: 340px; }
  .fold-right .service { left: 26px; }
  .service h2 {
    font-family: "Exo 2", sans-serif; font-weight: 600; font-size: 24px;
    color: var(--accent); line-height: 1; margin-bottom: 6px; letter-spacing: 0.1px;
  }
  .service p {
    font-family: "Arimo", sans-serif; font-size: 14.3px; line-height: 17.2px; color: var(--text);
  }
</style>
</head>
<body>
<main class="brochure">

  <section class="cover">
    <svg width="400" height="848" viewBox="0 0 400 848" aria-hidden="true">
      <path d="M400,666 C350,712 300,728 220,731 C110,735 45,755 0,786 V848 H400 Z" fill="#ffffff"/>
    </svg>
    <div class="company-name">Pim Tavel Marketing</div>
  </section>

  <section class="fold fold-middle">
    <svg width="384" height="848" viewBox="0 0 384 848" aria-hidden="true">
      <defs>
        <linearGradient id="fold-shade-mid" x1="0" y1="0" x2="0" y2="1">
          <stop offset="0" stop-color="#040606"/>
          <stop offset="1" stop-color="#1f2326"/>
        </linearGradient>
      </defs>
      <path d="M0,0 H384 V382 C330,418 262,437 180,439 C92,441 38,452 0,481 Z" fill="url(#fold-shade-mid)"/>
    </svg>

    <article class="service" style="top:46px">
      <h2>Corporate Branding</h2>
      <p>Lorem ipsum dolor sit amet, consectetuer adipisc-<br>ing elit. Ut nisi. Aenean aliquet nibh in ipsum.<br>Vivamus ultricies urna id ante. Ut lacus diam,<br>cursus eu, elementum id, placerat non, augue.<br>Proin laoreet, nisi ac eleifend volutpat.</p>
    </article>
    <article class="service" style="top:242px">
      <h2>Marketing</h2>
      <p>Lorem ipsum dolor sit amet, consectetuer adipisc-<br>ing elit. Ut nisi. Aenean aliquet nibh in ipsum.<br>Vivamus ultricies urna id ante. Ut lacus diam,<br>cursus eu, elementum id, placerat non, augue.<br>Proin laoreet, nisi ac eleifend volutpat.</p>
    </article>
    <article class="service" style="top:438px">
      <h2>Web Design</h2>
      <p>Lorem ipsum dolor sit amet, consectetuer adipisc-<br>ing elit. Ut nisi. Aenean aliquet nibh in ipsum.<br>Vivamus ultricies urna id ante. Ut lacus diam,<br>cursus eu, elementum id, placerat non, augue.<br>Proin laoreet, nisi ac eleifend volutpat.</p>
    </article>
    <article class="service" style="top:635px">
      <h2>Business Consultation</h2>
      <p>Lorem ipsum dolor sit amet, consectetuer adipisc-<br>ing elit. Ut nisi. Aenean aliquet nibh in ipsum.<br>Vivamus ultricies urna id ante. Ut lacus diam,<br>cursus eu, elementum id, placerat non, augue.<br>Proin laoreet, nisi ac eleifend volutpat.</p>
    </article>
  </section>

  <section class="fold fold-right">
    <svg width="400" height="848" viewBox="0 0 400 848" aria-hidden="true">
      <defs>
        <linearGradient id="fold-shade-right" x1="0" y1="0" x2="0" y2="1">
          <stop offset="0" stop-color="#040606"/>
          <stop offset="1" stop-color="#1f2326"/>
        </linearGradient>
      </defs>
      <path d="M0,0 H400 V382 C344,418 272,437 188,439 C96,441 40,452 0,481 Z" fill="url(#fold-shade-right)"/>
    </svg>

    <article class="service" style="top:103px">
      <h2>Printing</h2>
      <p>Lorem ipsum dolor sit amet, consectetuer adipisc-<br>ing elit. Ut nisi. Aenean aliquet nibh in ipsum.<br>Vivamus ultricies urna id ante. Ut lacus diam,<br>cursus eu, elementum id, placerat non, augue.<br>Proin laoreet, nisi ac eleifend volutpat.</p>
    </article>
    <article class="service" style="top:300px">
      <h2>Mailing</h2>
      <p>Lorem ipsum dolor sit amet, consectetuer adipisc-<br>ing elit. Ut nisi. Aenean aliquet nibh in ipsum.<br>Vivamus ultricies urna id ante. Ut lacus diam,<br>cursus eu, elementum id, placerat non, augue.<br>Proin laoreet, nisi ac eleifend volutpat.</p>
    </article>
    <article class="service" style="top:497px">
      <h2>Automation</h2>
      <p>Lorem ipsum dolor sit amet, consectetuer adipisc-<br>ing elit. Ut nisi. Aenean aliquet nibh in ipsum.<br>Vivamus ultricies urna id ante. Ut lacus diam,<br>cursus eu, elementum id, placerat non, augue.<br>Proin laoreet, nisi ac eleifend volutpat.</p>
    </article>
    <article class="service" style="top:694px">
      <h2>Pim Tavel Choice</h2>
      <p>Lorem ipsum dolor sit amet, consectetuer adipisc-<br>ing elit. Ut nisi. Aenean aliquet nibh in ipsum.<br>Vivamus ultricies urna id ante. Ut lacus diam,<br>cursus eu, elementum id, placerat non, augue.<br>Proin laoreet, nisi ac eleifend volutpat.</p>
    </article>
  </section>

</main>
</body>
</html>
```